Flyer-Design für Verlegung von fugenlosen Böden
Zielgruppe
Die Firma KORVAL, hat seinen Hauptaugenmerk auf das verlegen von fugenlosen Böden gelegt.
welchen Vorteil bietet Ihnen dieser Bodenbelag? Der fugenlose Bodenbelag wie der Epoxidharzboden oder der Steinteppich ist in den letzten Jahren eine beliebte Alternative zu Laminat, Fliesen, Parkett und anderen Bodenbelägen geworden.Seine steigende Beliebtheit verdankt der fugenlose Bodenbelag unter anderem seiner Robustheit.Unsere Bodenbeläge sind Geruchsneutral und bietet eine lange Lebensdauer. Die Zielgruppe sind Private sowie Gewerbliche Kunden.
Aufgabenstellung
Der Text sollte den effekt, 'Wow' das muss ich haben beim Leser auslösen. Das gleiche zählt für die verwendeten Bilder die der Desinger gerne auswählen derf. Mehr Infos Z.b Logo kann sich der Desinger auf der Webseite entnehmen.
www.korval-estrich.example

```html
<!DOCTYPE html>
<html lang="de">
<head>
<meta charset="utf-8">
<title>KORVAL – Fugenlose Bodenbeläge</title>
<link href="https://fonts.googleapis.com/css2?family=Open+Sans:wght@400;600;700&family=PT+Sans+Narrow:wght@400&display=swap" rel="stylesheet">
<style>
  :root {
    --orange: #c84a08;
    --orange-text: #c44a10;
    --slate-light: #8aa3bd;
    --slate-dark: #5d7a98;
    --ink: #4a4a4a;
    --logo-grey: #3f4649;
    --white: #ffffff;
  }
  * { box-sizing: border-box; margin: 0; padding: 0; }
  html, body { width: 1200px; height: 846px; overflow: hidden; }
  body { font-family: "Open Sans", sans-serif; }
  .flyer {
    position: relative; width: 1200px; height: 846px; overflow: hidden;
    background: radial-gradient(ellipse at 35% 40%, var(--slate-light), var(--slate-dark) 85%);
  }
  .brand {
    position: absolute; left: 49px; top: 46px;
    display: flex; align-items: center; gap: 14px;
    font-family: "Open Sans", sans-serif; font-weight: 700;
    font-size: 78px; letter-spacing: 4px; color: var(--logo-grey); line-height: 1;
  }
  .brand-mark { width: 22px; height: 22px; background: var(--orange); }
  .contact {
    position: absolute; left: 49px; top: 178px; width: 380px;
    color: var(--white); font-size: 21.8px; line-height: 29px; white-space: nowrap;
  }
  .contact p + p { margin-top: 29px; }
  .portrait {
    position: absolute; left: 438px; top: 21px; width: 388px; height: 402px;
    border-radius: 160px 160px 0 0;
    background: linear-gradient(180deg, #6b4a38 0%, #d8b8a4 40%, #eeeeee 75%, #f4f4f4 100%);
  }
  .info-box {
    position: absolute; left: 44px; top: 422px; width: 751px; height: 391px;
    background: var(--white); padding: 16px 18px 0 18px;
  }
  .info-title {
    font-family: "PT Sans Narrow", sans-serif; font-weight: 400;
    font-size: 28.5px; color: var(--orange-text); line-height: 40px;
  }
  .info-text {
    margin-top: 24px;
    font-family: "PT Sans Narrow", sans-serif; font-size: 21.5px;
    line-height: 29px; color: var(--ink); white-space: nowrap;
  }
  .benefits {
    position: absolute; left: 834px; top: 0; width: 366px; height: 846px;
    background: var(--orange); list-style: none;
  }
  .benefit {
    position: absolute; left: 28px; display: flex; align-items: center;
    color: var(--white); font-size: 22px; line-height: 29px; white-space: nowrap;
  }
  .benefit svg { width: 46px; height: 42px; flex: none; margin-right: 18px; }
</style>
</head>
<body>
<main class="flyer">
  <div class="brand"><span class="brand-mark"></span>KORVAL</div>

  <div class="contact">
    <p>Lindenweg 12 | 54321 Musterfeld</p>
    <p>Mobil: 0170 00 00 000<br>Telefon: 01234 - 567 89 00</p>
    <p>E-Mail: fugenlos@korval.example<br>www.korval-estrich.example</p>
  </div>

  <div class="portrait" role="img" aria-label="Foto einer lächelnden jungen Frau mit Mütze, die mit beiden Händen nach rechts zeigt"></div>

  <section class="info-box">
    <h2 class="info-title">Warum ein fugenloser Boden?</h2>
    <p class="info-text">
      Je mehr unterschiedliche Materialien als Fußbodenbelag eingesetzt werden, desto kleiner und<br>
      unruhiger wirkt das gesamte Interieur. Der durchgehende, fugenlose Boden hingegen hält sich<br>
      elegant im Hintergrund und schafft eine ruhige Atmosphäre. Keine ablenkenden Muster oder<br>
      Absätze stören das Bild, wodurch kleine Räume größer wirken. Besonders toll kommt das auch<br>
      in offenen Küchen mit anschließendem Wohn-Ess-Bereich zur Geltung.<br>
      Einer der wichtigsten Vorteile gegenüber vielen anderen Bodenbelägen ist, dass der fugenlose<br>
      Boden besonders robust und leicht zu pflegen ist. Er wird mit mehreren Schichten versiegelt und<br>
      hat keine störenden Fugen. Anders als bei Parkett, Laminat ,Fliesen oder Vinyl ist er unempfind-<br>
      lich gegen Kratzer und Stöße.
    </p>
  </section>

  <svg width="0" height="0" style="position:absolute">
    <symbol id="tick" viewBox="0 0 46 42">
      <path d="M36 14 A18 18 0 1 1 30 7" fill="none" stroke="#fff" stroke-width="3.5" stroke-linecap="round"/>
      <path d="M12 21 L20 29 L43 4" fill="none" stroke="#fff" stroke-width="4" stroke-linecap="round" stroke-linejoin="round"/>
    </symbol>
  </svg>

  <ul class="benefits">
    <li class="benefit" style="top:89px"><svg><use href="#tick"/></svg><span>Dem Design sind keine<br>Grenzen gesetzt</span></li>
    <li class="benefit" style="top:176px"><svg><use href="#tick"/></svg><span>Freie Farbauswahl aus<br>über 200 Farben<br>(metallic,matt)</span></li>
    <li class="benefit" style="top:292px"><svg><use href="#tick"/></svg><span>Ihr Persönliches<br>Einzelstück</span></li>
    <li class="benefit" style="top:379px"><svg><use href="#tick"/></svg><span>Weil Ihr Boden kein<br>Standart Boden<br>werden soll!</span></li>
    <li class="benefit" style="top:495px"><svg><use href="#tick"/></svg><span>Der Boden mit dem<br>Wow Effekt!</span></li>
    <li class="benefit" style="top:582px"><svg><use href="#tick"/></svg><span>Geben Sie sich nicht<br>mit weniger zufrieden!</span></li>
    <li class="benefit" style="top:669px"><svg><use href="#tick"/></svg><span>Hochglanz&nbsp; oder Matt<br>Versiegelung</span></li>
  </ul>
</main>
</body>
</html>
```